High-End Bifold Brochure for Aesthetics Medspa Business

I need a print-ready, bifold brochure designed for a high-end, luxurious Aesthetics/Medspa practice.

The brochure will showcase the latest IV Therapy content (6 options included in MENU.docx), and exclusive Vitamin B12+ wellness shot content (included in VB PDF). It should also include the business logo and basic office contact options.

The design should be clean, modern, and appealing with a light design. It should flow nicely and compliment the website theme/design. Preferably, having the 6 IV treatments inside bifold, with B12 shot on back/outside page. For easy viewing.

I have attached a few licensed images, if you think they will incorporate into the design nicely. Otherwise, please ignore them. If needed, I can send more.

https://velorabloomclinic.com/
Brand purple: #491c64
Fonts used on site:
Josefin Sans
Montserrat

Size should be 6.5 x 9 using specs on Quellpress's template page (Half Fold design)
https://www.quellpress.com/resources/templates

Font styles to use
Other font styles liked:
• Montserrat, Josefin Sans, or similar

Requirements
Must have
• Content included in MENU + B12 shot content on PDF.
Similar feel to the website, High-end, modern, luxurious

```html
<!DOCTYPE html>
<html lang="en">
<head>
<meta charset="utf-8">
<title>Velora Bloom Clinic — IV Therapy Brochure</title>
<link rel="stylesheet" href="https://fonts.googleapis.com/css2?family=Montserrat:wght@400;500;600;700&family=Josefin+Sans:wght@400;600;700&family=Oswald:wght@500;600&display=swap">
<style>
  :root{
    --plum:#491c64;
    --violet:#6a2c91;
    --violet-light:#8a4bb5;
    --orange:#f29a38;
    --orange-light:#f8c36a;
    --mist:#e4e4e7;
    --paper:#ffffff;
    --stage:#f2f2f2;
    --ink:#1c1c1e;
    --body:#3c3c40;
    --rule:#9a9aa0;
  }
  *{box-sizing:border-box;margin:0;padding:0}
  html,body{width:1200px;height:900px;overflow:hidden;background:var(--stage)}
  body{font-family:"Montserrat",sans-serif;color:var(--ink);position:relative}

  .spread{position:absolute;top:55px;width:575px;height:790px;display:flex;box-shadow:0 10px 28px rgba(0,0,0,.12)}
  .spread--outside{left:10px}
  .spread--inside{left:615px}
  .panel{position:relative;width:50%;height:100%;overflow:hidden;background:var(--paper)}
  .panel__art{position:absolute;inset:0;width:100%;height:100%}

  /* Back panel */
  .cta{position:absolute;left:0;right:0;top:26px;text-align:center}
  .cta__lead{font-family:"Josefin Sans",sans-serif;font-weight:700;font-size:17px;letter-spacing:.3px;color:var(--ink)}
  .cta__main{font-family:"Oswald",sans-serif;font-weight:600;font-size:27px;line-height:1.05;color:var(--ink);letter-spacing:.2px}
  .phone{position:absolute;left:36px;top:96px;width:228px;height:28px;border-radius:0 14px 14px 0;background:var(--plum);color:#fff;font-family:"Montserrat",sans-serif;font-weight:700;font-size:17px;line-height:28px;padding-left:42px}
  .phone__icon{position:absolute;left:-4px;top:-5px;width:38px;height:38px;border-radius:50%;background:#fff;border:2px solid var(--plum);display:flex;align-items:center;justify-content:center}
  .contact{position:absolute;left:0;right:0;bottom:18px;text-align:center;color:#fff;font-size:10.5px;line-height:1.5}
  .contact__pin{display:block;margin:0 auto 2px}
  .contact__email{margin-top:8px}
  .social{display:flex;justify-content:center;gap:6px;margin-top:10px}
  .social span{width:16px;height:16px;border-radius:50%;background:#fff}

  /* Front panel */
  .brand{position:absolute;top:38px;left:0;right:0;display:flex;align-items:center;justify-content:center;gap:8px}
  .brand__mark{width:14px;height:14px;border-radius:50%;background:var(--plum)}
  .brand__name{font-family:"Josefin Sans",sans-serif;font-weight:700;font-size:19px;color:var(--plum);letter-spacing:.4px}
  .cover-title{position:absolute;left:0;right:0;bottom:22px;text-align:center;color:#fff}
  .cover-title__city{font-family:"Josefin Sans",sans-serif;font-weight:700;font-size:44px;line-height:1;letter-spacing:1px}
  .cover-title__sub{font-family:"Josefin Sans",sans-serif;font-weight:600;font-size:22px;letter-spacing:1.4px;margin-top:4px}
  .cover-title__rule{width:70px;height:1px;background:rgba(255,255,255,.7);margin:14px auto 12px}
  .cover-title__web{font-size:10.5px;letter-spacing:1px}
  .cover-title__web b{font-weight:600}

  /* Inside panels */
  .panel--menu,.panel--b12{padding:28px 18px 18px 20px;display:flex;flex-direction:column;background:linear-gradient(100deg,#fafafa,#fff 60%,#f1f1f3)}
  .menu-title{font-family:"Josefin Sans",sans-serif;font-weight:700;font-size:22px;letter-spacing:.8px;color:var(--ink);line-height:1;white-space:nowrap}
  .menu-banner{margin-top:4px;background:var(--plum);color:#fff;font-family:"Josefin Sans",sans-serif;font-weight:700;font-size:21px;letter-spacing:5px;text-align:center;padding:5px 0 2px}
  .menu{flex:1;display:flex;flex-direction:column;justify-content:space-between;margin-top:18px}
  .item__head{display:flex;align-items:flex-end;gap:6px;border-bottom:1px solid var(--rule);padding-bottom:3px;margin-bottom:6px;position:relative}
  .item__name{flex:1;font-family:"Josefin Sans",sans-serif;font-weight:600;font-size:12.5px;line-height:1.15;color:var(--plum);letter-spacing:.3px}
  .item__price{background:var(--plum);color:#fff;font-weight:700;font-size:14px;padding:3px 10px 3px 18px;clip-path:polygon(12px 0,100% 0,100% 100%,0 100%);margin-bottom:-4px}
  .item__text{font-size:7.8px;line-height:1.32;color:var(--body);text-align:justify}

  .b12-title{font-family:"Josefin Sans",sans-serif;font-weight:700;font-size:21px;letter-spacing:.6px;line-height:1;white-space:nowrap}
  .b12-banner{margin-top:4px;background:var(--plum);color:#fff;font-family:"Josefin Sans",sans-serif;font-weight:700;font-size:10.2px;line-height:1.35;letter-spacing:.3px;padding:7px 8px 5px;white-space:nowrap}
  .nutrients{list-style:none;margin-top:14px;display:flex;flex-direction:column;gap:11px}
  .nutrients li{display:flex;gap:7px;font-size:7.8px;line-height:1.35;color:var(--body)}
  .nutrients b{color:var(--plum);font-weight:700}
  .check-ring{flex:none;width:10px;height:10px;margin-top:1px}
  .benefits-title{margin-top:22px;font-family:"Josefin Sans",sans-serif;font-weight:700;font-size:13px;color:var(--plum);letter-spacing:.5px;border-bottom:1px solid var(--rule);padding-bottom:3px}
  .benefits{list-style:none;margin-top:10px;display:flex;flex-direction:column;gap:9px}
  .benefits li{display:flex;gap:8px;font-size:7.8px;line-height:1.35;color:var(--body)}
  .tick{flex:none;width:9px;height:9px;margin-top:1px}
  .spread--inside::after{content:"";position:absolute;left:0;right:0;bottom:0;height:2px;background:var(--plum)}
</style>
</head>
<body>

<section class="spread spread--outside">
  <article class="panel panel--back">
    <svg class="panel__art" viewBox="0 0 288 790" preserveAspectRatio="none">
      <rect x="0" y="150" width="288" height="520" fill="#9a8478" role="img" aria-label="Photo area: warm salon interior behind the treatment scene"/>
      <circle cx="118" cy="430" r="142" fill="var(--plum)"/>
      <circle cx="118" cy="430" r="136" fill="#c9b3a4" role="img" aria-label="Photo: smiling client receiving an IV treatment"/>
      <path d="M0 0H288V200C200 190 100 230 0 140Z" fill="#fff"/>
      <path d="M0 128C70 170 150 200 288 168V210C170 232 90 210 0 160Z" fill="var(--violet)"/>
      <path d="M0 150C80 195 170 230 288 205V220C170 240 80 215 0 170Z" fill="var(--plum)"/>
      <path d="M0 620C110 612 200 580 288 540V580C190 620 100 650 0 655Z" fill="var(--orange)"/>
      <path d="M0 640C110 640 200 610 288 575V790H0Z" fill="var(--plum)"/>
    </svg>
    <div class="cta">
      <p class="cta__lead">CALL TODAY FOR YOUR</p>
      <p class="cta__main">FREE CONSULTATION</p>
    </div>
    <div class="phone">
      <span class="phone__icon">
        <svg width="18" height="18" viewBox="0 0 24 24"><path d="M6.6 10.8c1.4 2.8 3.8 5.2 6.6 6.6l2.2-2.2c.3-.3.7-.4 1-.2 1.1.4 2.3.6 3.6.6.6 0 1 .4 1 1V20c0 .6-.4 1-1 1C10.6 21 3 13.4 3 4c0-.6.4-1 1-1h3.5c.6 0 1 .4 1 1 0 1.3.2 2.5.6 3.6.1.3 0 .7-.2 1z" fill="var(--plum)"/></svg>
      </span>
      (555) 014-2290
    </div>
    <div class="contact">
      <svg class="contact__pin" width="10" height="13" viewBox="0 0 10 13"><path d="M5 0C2.2 0 0 2.2 0 5c0 3.5 5 8 5 8s5-4.5 5-8c0-2.8-2.2-5-5-5zm0 7a2 2 0 110-4 2 2 0 010 4z" fill="#fff"/></svg>
      <p>2180 N Marrow Ridge Rd, Suite 204</p>
      <p>Tucson, Arizona 85700</p>
      <p class="contact__email">&#9993; info@velorabloomclinic.com</p>
      <div class="social"><span></span><span></span><span></span><span></span></div>
    </div>
  </article>

  <article class="panel panel--cover">
    <svg class="panel__art" viewBox="0 0 287 790" preserveAspectRatio="none">
      <rect width="287" height="790" fill="var(--mist)"/>
      <rect x="0" y="150" width="287" height="520" fill="#d2b4a0" role="img" aria-label="Photo: portrait of a woman with clear, glowing skin"/>
      <path d="M0 0H287V140C200 150 110 210 0 200Z" fill="var(--mist)"/>
      <path d="M0 195C100 200 190 135 287 150V175C190 160 110 225 0 230Z" fill="var(--violet)"/>
      <path d="M0 650C90 590 200 590 287 650V675C200 620 100 625 0 680Z" fill="var(--orange)"/>
      <path d="M0 670C100 615 200 625 287 685V790H0Z" fill="var(--plum)"/>
    </svg>
    <div class="brand"><span class="brand__mark"></span><span class="brand__name">VELORA BLOOM CLINIC</span></div>
    <div class="cover-title">
      <p class="cover-title__city">TUCSON'S</p>
      <p class="cover-title__sub">PREMIER MEDSPA</p>
      <div class="cover-title__rule"></div>
      <p class="cover-title__web">www.<b>VeloraBloomClinic</b>.com</p>
    </div>
  </article>
</section>

<section class="spread spread--inside">
  <article class="panel panel--menu">
    <h1 class="menu-title">THE RENEW ROOM</h1>
    <p class="menu-banner">IV THERAPY</p>
    <div class="menu">
      <div class="item">
        <div class="item__head"><h2 class="item__name">IMMUNITY BOOSTER</h2><span class="item__price">$150</span></div>
        <p class="item__text">Have a cold, flu or just need to give your immunity a boost? Let us mix a powerful punch in our booster bag just for you to prevent or relieve aches and pain</p>
      </div>
      <div class="item">
        <div class="item__head"><h2 class="item__name">REFRESH &amp; HYDRATE</h2><span class="item__price">$100</span></div>
        <p class="item__text">Relieve dehydration from the extremes of lifestyle with our balanced electrolyte cocktail targeting jet lag, fatigue, stress and sports related activity to leave you feeling more youthful and refreshed!</p>
      </div>
      <div class="item">
        <div class="item__head"><h2 class="item__name">MIGRAINE BUSTER</h2><span class="item__price">$150</span></div>
        <p class="item__text">Eradicate your migraine pain, nausea, vomiting, and light sensitivity with our magic formula</p>
      </div>
      <div class="item">
        <div class="item__head"><h2 class="item__name">WELLNESS INFUSION:<br>Myer's Cocktail</h2><span class="item__price">$180</span></div>
        <p class="item__text">This infusion of vitamins, minerals and electrolytes results in direct access of these nutrients into your cells, enhancing energy, decreasing stress and anxiety in addition to improving memory. Other benefits include relief of asthma, depression, allergies and fibromyalgia pain</p>
      </div>
      <div class="item">
        <div class="item__head"><h2 class="item__name">GLO</h2><span class="item__price">$200</span></div>
        <p class="item__text">A Beauty mixture of Glutathione, Biotin and our special formula created to strengthen your hair, nails and skin for that SPECIAL LOOK!</p>
      </div>
      <div class="item">
        <div class="item__head"><h2 class="item__name">THE ULTIMATE WEIGHT<br>LOSS INFUSION</h2><span class="item__price">$180</span></div>
        <p class="item__text">Our unique fat burning formula targets fatty deposits resulting in fat expulsion from the body resulting in a more defined and contoured appearance.</p>
      </div>
      <div class="item">
        <div class="item__head"><h2 class="item__name">NAD+ IV: THE FOUNTAIN<br>OF YOUTH (+-)</h2><span class="item__price">$350</span></div>
        <p class="item__text">Anti-aging co-enzyme NAD+ in conjunction with Vitamins elevates brain health and beauty, all in one IV treatment!</p>
      </div>
    </div>
  </article>

  <article class="panel panel--b12">
    <h1 class="b12-title">DR. HALVERN'S</h1>
    <p class="b12-banner">VITAMIN B12 COCKTAIL'S<br>ESSENTIAL VITAMINS &amp; NUTRIENTS:</p>
    <ul class="nutrients">
      <li><svg class="check-ring" viewBox="0 0 10 10"><circle cx="5" cy="5" r="4.4" fill="none" stroke="var(--plum)" stroke-width=".9"/><path d="M3 5.1l1.4 1.4L7 3.8" fill="none" stroke="var(--plum)" stroke-width=".9"/></svg><span><b>Thiamine -</b> is used by the body to metabolize food for energy and maintain proper health and nerve function.</span></li>
      <li><svg class="check-ring" viewBox="0 0 10 10"><circle cx="5" cy="5" r="4.4" fill="none" stroke="var(--plum)" stroke-width=".9"/><path d="M3 5.1l1.4 1.4L7 3.8" fill="none" stroke="var(--plum)" stroke-width=".9"/></svg><span><b>Riboflavin -</b> acts as an antioxidant within the body. Riboflavin prevents free radical damage and protects skin and eye health.</span></li>
      <li><svg class="check-ring" viewBox="0 0 10 10"><circle cx="5" cy="5" r="4.4" fill="none" stroke="var(--plum)" stroke-width=".9"/><path d="M3 5.1l1.4 1.4L7 3.8" fill="none" stroke="var(--plum)" stroke-width=".9"/></svg><span><b>Niacinamide -</b> helps maintain a healthy cardiovascular system and metabolism, brain function, healthy skin formation, and aids in the prevention of and management of diabetes.</span></li>
      <li><svg class="check-ring" viewBox="0 0 10 10"><circle cx="5" cy="5" r="4.4" fill="none" stroke="var(--plum)" stroke-width=".9"/><path d="M3 5.1l1.4 1.4L7 3.8" fill="none" stroke="var(--plum)" stroke-width=".9"/></svg><span><b>Pyridoxine -</b> is important for brain development and keeping the nervous and immune systems healthy.</span></li>
      <li><svg class="check-ring" viewBox="0 0 10 10"><circle cx="5" cy="5" r="4.4" fill="none" stroke="var(--plum)" stroke-width=".9"/><path d="M3 5.1l1.4 1.4L7 3.8" fill="none" stroke="var(--plum)" stroke-width=".9"/></svg><span><b>Hydroxocobalamin -</b> helps with DNA synthesis and supports replication, it also helps in the body's use of fats and carbohydrates for energy, and in the making of new proteins.</span></li>
      <li><svg class="check-ring" viewBox="0 0 10 10"><circle cx="5" cy="5" r="4.4" fill="none" stroke="var(--plum)" stroke-width=".9"/><path d="M3 5.1l1.4 1.4L7 3.8" fill="none" stroke="var(--plum)" stroke-width=".9"/></svg><span><b>Methionine -</b> aids in tissue growth and repair, as well as promoting healthy hair, skin, and nails.</span></li>
      <li><svg class="check-ring" viewBox="0 0 10 10"><circle cx="5" cy="5" r="4.4" fill="none" stroke="var(--plum)" stroke-width=".9"/><path d="M3 5.1l1.4 1.4L7 3.8" fill="none" stroke="var(--plum)" stroke-width=".9"/></svg><span><b>Inositol -</b> aids in the metabolic breakdown of fats, and helps reduce blood cholesterol.</span></li>
      <li><svg class="check-ring" viewBox="0 0 10 10"><circle cx="5" cy="5" r="4.4" fill="none" stroke="var(--plum)" stroke-width=".9"/><path d="M3 5.1l1.4 1.4L7 3.8" fill="none" stroke="var(--plum)" stroke-width=".9"/></svg><span><b>L-carnitine -</b> helps convert fatty acids into energy.</span></li>
      <li><svg class="check-ring" viewBox="0 0 10 10"><circle cx="5" cy="5" r="4.4" fill="none" stroke="var(--plum)" stroke-width=".9"/><path d="M3 5.1l1.4 1.4L7 3.8" fill="none" stroke="var(--plum)" stroke-width=".9"/></svg><span><b>Chromium -</b> helps move sugars from the blood system, and turn fats, carbs, and proteins into energy.</span></li>
    </ul>
    <h2 class="benefits-title">OVERALL BENEFITS:</h2>
    <ul class="benefits">
      <li><svg class="tick" viewBox="0 0 10 10"><path d="M1 5.5l2.6 2.6L9 1.8" fill="none" stroke="var(--plum)" stroke-width="1.3"/></svg><span>B12 helps aid in red blood cell formation and in DNA synthesis</span></li>
      <li><svg class="tick" viewBox="0 0 10 10"><path d="M1 5.5l2.6 2.6L9 1.8" fill="none" stroke="var(--plum)" stroke-width="1.3"/></svg><span>Aids in the healthy maintenance of the immune and nervous systems, and the optic nerve</span></li>
      <li><svg class="tick" viewBox="0 0 10 10"><path d="M1 5.5l2.6 2.6L9 1.8" fill="none" stroke="var(--plum)" stroke-width="1.3"/></svg><span>Helps improve skin tone, and strengthen nails and hair</span></li>
      <li><svg class="tick" viewBox="0 0 10 10"><path d="M1 5.5l2.6 2.6L9 1.8" fill="none" stroke="var(--plum)" stroke-width="1.3"/></svg><span>Boosts metabolism and energy (which may help reduce craving and encourage weight loss)</span></li>
      <li><svg class="tick" viewBox="0 0 10 10"><path d="M1 5.5l2.6 2.6L9 1.8" fill="none" stroke="var(--plum)" stroke-width="1.3"/></svg><span>Helps relieve cramping and bloating</span></li>
      <li><svg class="tick" viewBox="0 0 10 10"><path d="M1 5.5l2.6 2.6L9 1.8" fill="none" stroke="var(--plum)" stroke-width="1.3"/></svg><span>Improves memory (which may protect against Alzheimer's)</span></li>
      <li><svg class="tick" viewBox="0 0 10 10"><path d="M1 5.5l2.6 2.6L9 1.8" fill="none" stroke="var(--plum)" stroke-width="1.3"/></svg><span>Enhances mood and lessens the effects of depression</span></li>
    </ul>
  </article>
</section>

</body>
</html>
```